Jewelry Manufacturing & Repair business needs advertising mailout - 9x4 flyer

Need new double sided flyer designed for an insert into a mailout. Want 9x4 (vertical design) to fit in 9.5" x 4.125" envelopes. Company based out of Louisiana called "Lem Tovick Manufacturing." Been in business for 45 years. We specialize in custom jewelry design and casting on the wholesale level. We are a full service trade shop offering CAD design, casting services, basic and advanced jewelry repair. Most of our customers are drawn to the fact that they talk directly with the owner/designer of the company each time they call. I've attached several images of CAD renders we've built and of our logo. I've also attached a copy of an old mailout we sent out 10 years ago that I designed myself (and it needed a lot of work). The business information listed in this old mailout is correct, except that we’ve been in business 45 years now. I would like the final design to be "business bold," portraying business strength and stability. I like shades of blue, or a gold/silver color scheme. Logo is black and white. Need double sided.

Looking for project to be less wordy than the 10 yr old mailout. Don’t need the “example scenario” in this flyer.
Updates

The weekend has made the 2 day timeframe very tight. Would like to extend timeframe, but I will select a design on Monday at 3:00 pm (USA Central time).

Target Market(s)

Retail Jewelry Stores

Industry/Entity Type

Jewelry

Colors
cfdeed
0455a3
3176b5
85acd3

Requirements
Must have
• All contact information.
Nice to have
• Purpose of this flyer is to get new accounts for our business. We want something that the retail jewelry store will notice something that will make them not throw away immediately, but instead hold onto for the future.
• This upcoming Christmas season is usually very busy for retail stores, so we can help take some of the overflow of work and still meet deadlines. With our help, they shouldn't have to turn any customer away.
Should not have
• We will be partnering in this mailout with a sister wholesale diamond company. Therefore, we don't want to mention that our company sells any diamonds, as we want to leave that part up to our sister company.

```html
<!DOCTYPE html>
<html lang="en">
<head>
<meta charset="utf-8">
<title>Lem Tovick Manufacturing – Flyer</title>
<link href="https://fonts.googleapis.com/css2?family=Source+Sans+3:wght@400;700&display=swap" rel="stylesheet">
<style>
  :root {
    --blue-deep: #0455a3;
    --blue-mid: #3176b5;
    --blue-soft: #85acd3;
    --blue-pale: #cfdeed;
    --white: #ffffff;
    --ink: #111111;
  }
  html, body { margin: 0; padding: 0; overflow: hidden; }
  body { width: 1200px; height: 1200px; background: var(--blue-deep); }
  .flyer {
    position: relative; width: 1200px; height: 1200px; overflow: hidden;
    background: var(--blue-deep); color: var(--white);
    font-family: "Source Sans 3", sans-serif;
  }
  .header-stripe {
    position: absolute; left: 0; top: 94px; width: 1200px; height: 47px;
    background: var(--blue-mid);
  }
  .brand-box {
    position: absolute; left: 32px; top: 14px; width: 246px; height: 170px;
    background: var(--white); border: 3px solid var(--ink); border-radius: 3px;
    display: flex; align-items: center; justify-content: center;
  }
  .brand-name {
    color: var(--ink); font-weight: 400; font-size: 64px; letter-spacing: -1px;
  }
  .company-title {
    position: absolute; left: 360px; top: 22px; margin: 0;
    font-weight: 400; font-size: 66px; white-space: nowrap; line-height: 1;
  }
  .tagline {
    position: absolute; left: 366px; top: 99px; margin: 0;
    font-size: 34px; font-weight: 400; white-space: nowrap; line-height: 1;
    letter-spacing: -0.3px;
  }
  .hero { position: absolute; left: 0; top: 208px; }
  .question {
    position: absolute; left: 912px; top: 432px; width: 368px; height: 368px;
    border-radius: 50%; background: var(--blue-deep);
    border: 6px solid var(--blue-soft); box-sizing: border-box;
  }
  .question-text {
    position: absolute; left: 940px; top: 532px; width: 330px; margin: 0;
    text-align: center; font-size: 40px; line-height: 53px; white-space: nowrap;
  }
  .question-text strong { font-weight: 700; }
  .intro { position: absolute; left: 35px; top: 804px; width: 540px; }
  .intro h2 { margin: 0 0 22px; font-size: 41px; font-weight: 700; line-height: 1.1; }
  .intro p { margin: 0; font-size: 28.5px; line-height: 39px; }
  .divider {
    position: absolute; left: 595px; top: 794px; width: 3px; height: 356px;
    background: var(--white);
  }
  .research {
    position: absolute; left: 632px; top: 842px; width: 640px; margin: 0;
    font-size: 28.5px; line-height: 39px; white-space: nowrap;
  }
  .phone {
    position: absolute; left: 968px; top: 1134px; height: 46px; padding: 0 0 0 12px;
    background: var(--blue-mid); font-weight: 700; font-size: 52px; line-height: 46px;
    white-space: nowrap; width: 300px;
  }
</style>
</head>
<body>
<div class="flyer">
  <div class="header-stripe"></div>
  <div class="brand-box"><span class="brand-name">LT mfg</span></div>
  <h1 class="company-title">Lem Tovick Manufacturing, LLC</h1>
  <p class="tagline">TOP QUALITY CRAFTSMANSHIP, FRIENDLY PERSONAL SERVICE</p>

  <svg class="hero" width="1200" height="560" viewBox="0 0 1200 560" aria-hidden="false">
    <defs>
      <radialGradient id="benchTone" cx="45%" cy="40%" r="75%">
        <stop offset="0" stop-color="#8a8a86"/>
        <stop offset="0.45" stop-color="#4c5257"/>
        <stop offset="1" stop-color="#2c3238"/>
      </radialGradient>
    </defs>
    <rect role="img" aria-label="Photo of a silver ring with a blue stone resting on a small jeweler's anvil on a workbench" x="0" y="0" width="1200" height="560" fill="url(#benchTone)"/>
    <path d="M0 544 C 300 530, 650 510, 1200 430 L1200 560 L0 560 Z" fill="var(--blue-deep)"/>
  </svg>

  <div class="question"></div>
  <p class="question-text"><strong>Are you looking</strong><br>for a way to<br>increase profits?</p>

  <section class="intro">
    <h2>Lem Tovick Manufacturing</h2>
    <p>can provide that highly skilled jeweler needed to take your business to the next level. We will work directly with you to meet all your customer’s needs, while maintaining a personal level of service that you will enjoy.</p>
  </section>

  <div class="divider"></div>

  <p class="research">Recent research shows that a large percentage of<br>customers who actively seek out a new jeweler<br>do so because they need some type of repair.<br>Additionally, customer loyalty and satisfaction is<br>based on a store’s ability to offer a complete line<br>of services.</p>

  <div class="phone">1-888-555-0142</div>
</div>
</body>
</html>
```